Flyer-Design für Immobilienmakler
Zielgruppe
Wir sind Immobilienmakler und die Zielgruppe sind Immobilieneigentümer. Mit dem Flyer wollen wir kreative und evtl. auch 'freche' art auf uns aufmernksammachen, dass der Verkaufwillige sich an uns wendet.
Aufgabenstellung
Was wir nicht wollen: Flyer wie sie alle machen...ala wir sind die Tollsten und Besten.
Die Flyerform kann gerne besonders sein.
Unser Farben:
Blau R33 G49 B98
Rot R201 G0 B25
Unsere 'Wanda' und das Logo sende ich Ihnen als JPG.
Die Vektordatei reiche ich nach

```html
<!DOCTYPE html>
<html lang="de">
<head>
<meta charset="utf-8">
<title>Giebel Immobilien – Flyer</title>
<link rel="stylesheet" href="https://fonts.googleapis.com/css2?family=Didact+Gothic&family=Quicksand:wght@600;700&display=swap">
<style>
  :root{
    --blue:#342e62;
    --red:#c9121b;
    --white:#ffffff;
    --page:#ffffff;
    --text:#2b2a3a;
  }
  *{box-sizing:border-box;margin:0;padding:0}
  html,body{width:1200px;height:1200px;overflow:hidden;background:var(--page)}
  body{position:relative;font-family:"Didact Gothic",sans-serif;color:var(--text)}
  .panel{position:absolute;background:var(--white);overflow:hidden;box-shadow:2px 3px 6px rgba(0,0,0,.35)}
  .panel--cover{left:27px;top:44px;width:715px;height:357px}
  .panel--back{left:809px;top:44px;width:350px;height:360px}
  .panel--inner{left:27px;top:450px;width:718px;height:358px}
  .panel--contact{left:809px;top:450px;width:348px;height:358px}

  .blue-band{position:absolute;left:0;right:0;bottom:0;background:var(--blue)}
  .headline{font-family:"Quicksand",sans-serif;font-weight:700;color:var(--blue);text-align:center;position:absolute}
  .company{font-size:17.5px}
  .rule{position:absolute;height:2px;background:var(--blue)}
  .tagline{font-size:17.5px}
  .tagline .accent{color:var(--red)}

  .brand{position:absolute;top:14px;display:flex;align-items:center;gap:6px;font-family:"Quicksand",sans-serif;font-weight:700;font-size:15px;color:var(--blue)}
  .brand__dot{width:7px;height:7px;border-radius:50%;background:var(--red)}

  .photo{position:absolute}
  .photo--peek{background:linear-gradient(180deg,#ffffff 0%,#f3ede8 40%,#c9a58d 100%)}
  .photo--house{left:0;top:0;width:718px;height:119px;background:linear-gradient(90deg,#5f6e3a 0%,#d9d6cf 30%,#e8e6e2 55%,#8b6a3e 80%,#6d7d3e 100%)}

  .callout{position:absolute;font-family:"Quicksand",sans-serif;font-weight:700;color:var(--white);font-size:16px;line-height:22px}
  .callout span{display:inline-block;background:var(--red);padding:2px 10px}
  .callout__lead{width:256px;padding:5px 10px;background:var(--red)}
  .callout__cta{position:absolute;text-transform:uppercase;background:var(--red);padding:3px 10px;white-space:nowrap}

  .office{position:absolute;font-size:8px;line-height:9.3px;color:var(--white)}
  .office__title{font-family:"Quicksand",sans-serif;font-weight:700;font-size:7.5px;letter-spacing:.2px;text-transform:uppercase;margin-bottom:10px}
  .office__name{margin-bottom:9px}

  .column{position:absolute;top:134px;width:157px;font-size:7.9px;line-height:9.25px;color:var(--text)}
  .column h3{font-family:"Quicksand",sans-serif;font-weight:700;font-size:7.5px;color:var(--blue);text-transform:uppercase;margin:0 0 6px}
  .column p{margin-bottom:12px}
</style>
</head>
<body>

<section class="panel panel--cover">
  <div class="headline company" style="left:0;width:358px;top:62px">Giebel Immobilien GmbH</div>
  <div class="rule" style="left:132px;top:93px;width:93px"></div>
  <div class="headline tagline" style="left:0;width:358px;top:106px">Besser w<span class="accent">o</span>hnen – Besser leben!</div>
  <div class="brand" style="left:600px"><span class="brand__dot"></span>Giebel Immobilien</div>
  <div class="photo photo--peek" role="img" aria-label="Mann mit Brille, der über den Rand des Flyers lugt" style="left:379px;top:78px;width:313px;height:101px"></div>
  <div class="blue-band" style="top:179px"></div>
  <div class="office" style="left:42px;top:246px">
    <div class="office__title">Hauptgeschäftsstelle Heidedorf</div>
    <div class="office__name">Giebel Immobilien GmbH</div>
    Lindenweg 12<br>21000 Heidedorf<br>info@giebel-immobilien-beispiel.de<br>Tel.&nbsp; +49 4100-123 45 60<br>Fax. +49 4100-123 45 61
  </div>
  <div class="office" style="left:197px;top:246px">
    <div class="office__title">Filiale Elbstadt</div>
    <div class="office__name">Giebel Immobilien GmbH</div>
    Am Markt 21<br>21600 Elbstadt<br>elbstadt@giebel-immobilien-beispiel.de<br>Tel.&nbsp; +49 4160-987 6500<br>Fax. +49 4160-987 6501
  </div>
  <div class="callout" style="left:402px;top:231px">
    <div class="callout__lead">Damit Ihnen der Haus verkauf nicht über den Kopf wächst.</div>
    <div class="callout__cta" style="left:53px;top:52px">Wir beraten Sie gerne!</div>
  </div>
</section>

<section class="panel panel--back">
  <div class="brand" style="left:210px"><span class="brand__dot"></span>Giebel Immobilien</div>
  <div class="photo photo--peek" role="img" aria-label="Mann mit Brille, der über den Rand des Flyers lugt" style="left:11px;top:78px;width:317px;height:102px"></div>
  <div class="blue-band" style="top:180px"></div>
  <div class="callout" style="left:34px;top:232px">
    <div class="callout__lead">Damit Ihnen der Haus verkauf nicht über den Kopf wächst.</div>
    <div class="callout__cta" style="left:54px;top:52px">Wir beraten Sie gerne!</div>
  </div>
</section>

<section class="panel panel--inner">
  <div class="photo photo--house" role="img" aria-label="Frau mit Verkauft-Schild, Einfamilienhaus mit Terrasse und Spielgerüst im Garten"></div>
  <div class="column" style="left:19px">
    <h3>Lorem ipsum</h3>
    <p>Lorem ipsum dolor sit amet, consectetuer adipiscing elit. Aenean commodo ligula eget dolor. Aenean massa. Cum sociis natoque penatibus et magnis dis parturient montes, nascetur ridiculus mus. Donec quam felis, ultricies nec, pellentesque eu, pretium quis, sem. Nulla consequat massa quis enim. Donec pede justo, fringilla vel, aliquet nec, vulputate eget, arcu. In enim justo, rhoncus ut, imperdiet a, venenatis vitae, justo. Nullam dictum felis eu pede mollis pretium. Integer tincidunt. Cras dapibus.</p>
    <h3>Lorem ipsum</h3>
    <p>Vivamus elementum semper nisi. Aenean vulputate eleifend tellus. Aenean leo ligula, porttitor eu, consequat vitae, eleifend ac, enim. Aliquam lorem ante, dapibus</p>
  </div>
  <div class="column" style="left:184px;top:136px">
    <p>in, viverra quis, feugiat a, tellus. Phasellus viverra nulla ut metus varius laoreet. Quisque rutrum. Aenean imperdiet. Etiam ultricies nisi vel augue. Curabitur ullamcorper ultricies nisi. Nam eget dui. Etiam rhoncus. Maecenas tempus, tellus eget condimentum rhoncus, sem quam semper libero, sit amet adipiscing sem neque sed ipsum.</p>
    <h3>Lorem ipsum</h3>
    <p>Nam quam nunc, blandit vel, luctus pulvinar, hendrerit id, lorem. Maecenas nec odio et ante tincidunt tempus. Donec vitae sapien ut libero venenatis faucibus. Nullam quis ante. Etiam sit amet orci eget eros faucibus tincidunt. Duis leo</p>
  </div>
  <div class="column" style="left:378px">
    <h3>Lorem ipsum</h3>
    <p>Lorem ipsum dolor sit amet, consectetuer adipiscing elit. Aenean commodo ligula eget dolor. Aenean massa. Cum sociis natoque penatibus et magnis dis parturient montes, nascetur ridiculus mus. Donec quam felis, ultricies nec, pellentesque eu, pretium quis, sem. Nulla consequat massa quis enim. Donec pede justo, fringilla vel, aliquet nec, vulputate eget, arcu. In enim justo, rhoncus ut, imperdiet a, venenatis vitae, justo. Nullam dictum felis eu pede mollis pretium. Integer tincidunt. Cras dapibus.</p>
    <h3>Lorem ipsum</h3>
    <p>Vivamus elementum semper nisi. Aenean vulputate eleifend tellus. Aenean leo ligula, porttitor eu, consequat vitae, eleifend ac, enim. Aliquam lorem ante, dapibus</p>
  </div>
  <div class="column" style="left:543px;top:136px">
    <p>in, viverra quis, feugiat a, tellus. Phasellus viverra nulla ut metus varius laoreet. Quisque rutrum. Aenean imperdiet. Etiam ultricies nisi vel augue. Curabitur ullamcorper ultricies nisi. Nam eget dui. Etiam rhoncus. Maecenas tempus, tellus eget condimentum rhoncus, sem quam semper libero, sit amet adipiscing sem neque sed ipsum.</p>
    <h3>Lorem ipsum</h3>
    <p>Nam quam nunc, blandit vel, luctus pulvinar, hendrerit id, lorem. Maecenas nec odio et ante tincidunt tempus. Donec vitae sapien ut libero venenatis faucibus. Nullam quis ante. Etiam sit amet orci eget eros faucibus tincidunt. Duis leo</p>
  </div>
</section>

<section class="panel panel--contact">
  <div class="headline company" style="left:0;width:348px;top:62px">Giebel Immobilien GmbH</div>
  <div class="rule" style="left:132px;top:93px;width:94px"></div>
  <div class="headline tagline" style="left:0;width:348px;top:106px">Besser w<span class="accent">o</span>hnen – Besser leben!</div>
  <div class="blue-band" style="top:180px"></div>
  <div class="office" style="left:42px;top:247px">
    <div class="office__title">Hauptgeschäftsstelle Heidedorf</div>
    <div class="office__name">Giebel Immobilien GmbH</div>
    Lindenweg 12<br>21000 Heidedorf<br>info@giebel-immobilien-beispiel.de<br>Tel.&nbsp; +49 4100-123 45 60<br>Fax. +49 4100-123 45 61
  </div>
  <div class="office" style="left:197px;top:247px">
    <div class="office__title">Filiale Elbstadt</div>
    <div class="office__name">Giebel Immobilien GmbH</div>
    Am Markt 21<br>21600 Elbstadt<br>elbstadt@giebel-immobilien-beispiel.de<br>Tel.&nbsp; +49 4160-987 6500<br>Fax. +49 4160-987 6501
  </div>
</section>

</body>
</html>
```